Audio Visual company needs brochure design

We are an AV company that does Audio Visual work solely for Commercial customers. We Design, sale and install various Audio Visual systems for our customers. This may be something as simple as a conference room, a new sound system for a church or a new sound, lighting and video system for an arena or stadium.

We don't really have any ideas in mind and that's the reason we are turning to you. We want something that highlights what we do, and something they will look at - not just toss in the can.

Included is a copy of our logo (sorry it's the only copy we have now)

Our company name is Kelvara Productions www.kelvaraproductions.com

Reason: The rest of our management team hasn't provided feedback to me yet. We will pick the design this week.

Target Market(s)

70% of our business is churches and the remaining is corporate customers and restaurants.

Industry/Entity Type

Church

Requirements
Must have
• The brochure will be 8.5" x 11" printed both sides - open to Z fold or Tri fold designs. We can provide pictures of our work if needed - though they may not be the best.
Should not have
• No generic pictures of just speakers, projectors, microphones, etc.

```html
<!DOCTYPE html>
<html lang="en">
<head>
<meta charset="utf-8">
<title>Kelvara Productions – Brochure Inside</title>
<link href="https://fonts.googleapis.com/css2?family=Roboto:wght@300&family=Oswald:wght@600&family=Tangerine:wght@400&display=swap" rel="stylesheet">
<style>
  :root {
    --bg: #1f1f1f;
    --text: #e6e6e6;
    --accent: #e0262b;
    --photo-red: #5a0c10;
  }
  html, body {
    margin: 0;
    padding: 0;
    overflow: hidden;
  }
  .brochure {
    position: relative;
    width: 1200px;
    height: 928px;
    background: var(--bg);
    overflow: hidden;
    font-family: "Roboto", Helvetica, Arial, sans-serif;
    font-weight: 300;
    color: var(--text);
  }
  .hero-photo {
    position: absolute;
    left: 0;
    top: 0;
    width: 460px;
    height: 440px;
    background:
      linear-gradient(to bottom, rgba(31,31,31,0) 45%, var(--bg) 100%),
      linear-gradient(to right, var(--photo-red) 0%, var(--photo-red) 55%, var(--bg) 100%);
  }
  .column {
    position: absolute;
  }
  .col-services { left: 68px; top: 401px; width: 258px; }
  .col-installations { left: 468px; top: 57px; width: 260px; }
  .col-rentals { left: 869px; top: 57px; width: 264px; }
  .column-title {
    font-family: "Tangerine", cursive;
    font-weight: 400;
    font-size: 64px;
    line-height: 64px;
    margin: 0 0 2px 0;
    color: #fff;
  }
  .section { margin: 0 0 15px 0; }
  .section-title {
    font-size: 14.5px;
    line-height: 15.2px;
    color: var(--accent);
    margin: 0;
    font-weight: 300;
  }
  .section p {
    font-size: 14.5px;
    line-height: 15.2px;
    margin: 0;
  }
  .tagline {
    position: absolute;
    left: 468px;
    top: 830px;
    margin: 0;
    font-family: "Oswald", "Arial Narrow", sans-serif;
    font-weight: 600;
    font-size: 16px;
    line-height: 19px;
    letter-spacing: 0;
    color: var(--accent);
    white-space: nowrap;
  }
</style>
</head>
<body>
<main class="brochure">
  <div class="hero-photo" role="img" aria-label="Photo of a stage spotlight in front of a red theatre curtain"></div>

  <section class="column col-services">
    <h2 class="column-title">services</h2>
    <div class="section">
      <h3 class="section-title">EVENT PRODUCTION</h3>
      <p>Kelvara has been a leader in the production industry. We are a full scale touring production company that owns and maintains an impressive inventory of the latest technology in audio, video, lighting and staging equipment. Kelvara can substantially cut your costs by being a one stop shop.</p>
    </div>
    <div class="section">
      <h3 class="section-title">REPAIRS</h3>
      <p>The Kelvara service department is second to none. Our service techs are responsible handles service calls and offers bench repair for most of the Pro audio, lighting &amp; video manufactures.</p>
    </div>
    <div class="section">
      <h3 class="section-title">CUSTOM FABRICATION</h3>
      <p>Kelvara has an in-house fabrication shop that supports our role as a full service AV and Production Company. Our fabrication shop is staffed by experienced carptners who have over 15 years experience.</p>
    </div>
  </section>

  <section class="column col-installations">
    <h2 class="column-title">instalations</h2>
    <div class="section">
      <h3 class="section-title">CHURCHES</h3>
      <p>As churches become larger and more advance with their teachings, so does the equipment requried to deliver that important message. Our engineers and technicians have experience in worship A/V not only because that is one of the largest shares of our business but because we are active in our own churches running the equipment.</p>
    </div>
    <div class="section">
      <h3 class="section-title">CORPORATE</h3>
      <p>We have worked with many corporate clients updating and intergrating new technology. From background music in a food chain to class rooms and board rooms, we've done it all. Working with you from the begining, our designers and project engineers ensure everything is in place during the critical times of construction. From rough-in to punch out, we are there every step of the way saving you valuable time and money.</p>
    </div>
    <div class="section">
      <h3 class="section-title">ENTERTAINMENT</h3>
      <p>Kelvara has been called on time and time again to design, install and fix Sound, Lighting and Video systems in many of the areas entertainment establishments. Our expertise have made us the favorite and in-house provider for many places.</p>
    </div>
    <div class="section">
      <h3 class="section-title">THE PROCESS</h3>
      <p>System intergration is not like it was once upon a time. AV systems have become sophisticated and peoples standards have grown dramatically. In the old days one would simply hang a speaker and aim it by what looked right with no thought of the room, it's contents and the people in mind.</p>
    </div>
  </section>

  <section class="column col-rentals">
    <h2 class="column-title">rentals</h2>
    <div class="section">
      <h3 class="section-title">SOUND</h3>
      <p>We have all the gear you need to be heard and the staff to run it! We carry all the big names including Harmona, Solvane, Barlow &amp; Finch, Trueline, Tonewright, Veltmark, Corvex, Ashgrove, Norvik, Reverin, Dalton and Kordia to name just a few. It doesn't matter if it's a crowd of 20 or 20,000-We have the gear requried to handle your event indoors and out!</p>
    </div>
    <div class="section">
      <h3 class="section-title">LIGHTING</h3>
      <p>We provide accent lighting for Weddings, Corporate and Tradeshow events and theatrical lighting for shows.</p>
    </div>
    <div class="section">
      <h3 class="section-title">VIDEO</h3>
      <p>We offer Projectors, Plasmas, LCD monitors, Screens, video switchers and media servers. For more information on the gear we stock.</p>
    </div>
    <div class="section">
      <h3 class="section-title">STAGING</h3>
      <p>We offers a large selection of Staging and Trussing. Kelvara uses Riserline and Platform Works stages, Tensor Rigging, Trussmark and Spanwell truss and Liftrite motors.</p>
    </div>
    <div class="section">
      <h3 class="section-title">MISC.</h3>
      <p>We offers everything you need to support your show. Power distros for FOH &amp; Lighting, Cable ramps to cover the cabling, Bicycle rack barricades, Intercom and Two-way radios.</p>
    </div>
    <div class="section">
      <h3 class="section-title">WEDDING</h3>
      <p>We offer everything from a simple powered speaker with a wireless mic for your officiant to use at your ceremony to lighting packages used to transform your reception into something never seen!</p>
    </div>
  </section>

  <p class="tagline">We specialize in all aspects of sound reinforcement, lighting, video and staging systems<br>in both the installation and production markets.</p>
</main>
</body>
</html>
```